Webdesign Birkental

Conversion of the site https://www.gasthaus-birkental.de/ The Deisgn should be modern and according to the latest stadtard SEO etc.

```html
<!DOCTYPE html>
<html lang="en">
<head>
<meta charset="utf-8">
<title>Gasthaus Birkental</title>
<link href="https://fonts.googleapis.com/css2?family=Montserrat:wght@400;500;600;700;800&display=swap" rel="stylesheet">
<style>
:root{
  --red:#d4123f;
  --green:#74b844;
  --ink:#111;
  --text:#555;
  --grey:#f2f2f2;
  --dark:#2b2b2b;
  --white:#fff;
}
*{margin:0;padding:0;box-sizing:border-box}
html,body{width:720px;height:1200px;overflow:hidden;background:var(--white)}
body{position:relative;font-family:'Montserrat',sans-serif;color:var(--ink)}
.abs{position:absolute}
.brand{font-weight:800;color:var(--red);letter-spacing:.3px;line-height:1}
.top-links{top:10px;right:185px;font-size:5.5px;font-weight:500;display:flex;gap:9px;white-space:nowrap}
.flags{top:9px;left:544px;display:flex;gap:2px}
.flags span{width:10px;height:7px;display:block}
.contact-line{top:24px;right:140px;font-size:8px;font-weight:700;white-space:nowrap}
.contact-line b{color:var(--red);font-size:11.5px;font-weight:600;letter-spacing:.3px}
.email-line{top:35px;right:140px;font-size:6px;letter-spacing:.5px;color:#333;white-space:nowrap}
.nav{top:48px;left:0;width:720px;height:18px;background:var(--green)}
.nav ul{list-style:none;display:flex;height:100%;margin-left:148px}
.nav li{font-size:5.6px;font-weight:600;color:var(--white);height:100%;display:flex;align-items:center;padding:0 18px;border-right:1px solid rgba(255,255,255,.35);transform:skewX(-20deg);white-space:nowrap}
.nav li span{transform:skewX(20deg)}
.nav li.active{background:var(--red)}
.hero-left{top:66px;left:0;width:403px;height:225px;background:linear-gradient(90deg,#c8183f,#d23b5d 70%,#cc2a50)}
.hero-photo{top:66px;left:403px;width:317px;height:225px;background:linear-gradient(160deg,#f28a1c,#e9a46a 40%,#c9a792 70%,#b77a56)}
.hero-title{top:105px;left:141px;font-size:24px;font-weight:800;color:var(--white);padding-left:16px;border-left:7px solid var(--green);line-height:26px}
.hero-sub{top:137px;left:141px;width:260px;font-size:12px;font-weight:700;color:var(--white);line-height:13.5px}
.hero-text{top:168px;left:142px;width:260px;font-size:12px;font-weight:400;color:var(--white);line-height:13.5px}
.btn{background:var(--green);color:var(--white);font-weight:600;display:flex;align-items:center;justify-content:center;clip-path:polygon(10px 0,100% 0,calc(100% - 10px) 100%,0 100%)}
.hero-btn{top:208px;left:142px;width:82px;height:19px;font-size:8px}
.dots{top:258px;left:539px;display:flex;gap:6px}
.dots span{width:10px;height:10px;background:var(--white)}
.dots span.on{border:2px solid var(--white);background:var(--red)}
.about{top:259px;left:141px;width:289px;height:166px;background:var(--white)}
.about h2{position:absolute;top:19px;left:18px;font-size:12px;font-weight:700;color:var(--red);padding-left:9px;border-left:2px solid var(--green);line-height:9px}
.about h3{position:absolute;top:35px;left:18px;font-size:7.5px;font-weight:700}
.about p{position:absolute;left:18px;width:262px;font-size:7.5px;line-height:11.3px;color:var(--text);letter-spacing:.15px}
.about .p1{top:49px}.about .p2{top:105px}
.about-btn{top:397px;left:157px;width:82px;height:19px;font-size:8px}
.about-photo{top:320px;left:430px;width:150px;height:85px;background:linear-gradient(135deg,#e98a2a,#c89070 45%,#6b3c22 80%)}
.services{top:433px;left:0;width:720px;height:190px;background:linear-gradient(180deg,#f6f6f6,#fff 40%)}
.services h2{position:absolute;top:22px;width:100%;text-align:center;font-size:16px;font-weight:700}
.services .rule{position:absolute;top:46px;left:351px;width:19px;height:2px;background:var(--red)}
.svc{top:503px;width:139px;height:86px}
.svc-label{top:597px;width:139px;text-align:center;font-size:9px;font-weight:600;color:var(--green)}
.gal-band{top:640px;left:0;width:329px;height:46px;background:var(--green)}
.gal-band h2{position:absolute;top:15px;left:141px;font-size:15px;font-weight:700;color:var(--white);letter-spacing:.3px;display:flex;align-items:center;gap:8px}
.gal-photo{top:686px;left:0;width:329px;height:180px;background:linear-gradient(90deg,#d8d6d2 0 90px,#6e5a4c 90px,#4d3a31 50%,#8e6a5a)}
.gal-grey{top:656px;left:329px;width:391px;height:194px;background:var(--grey)}
.thumb{width:74px;height:70px}
.info{top:870px;font-size:6.3px;font-weight:600;line-height:9px;display:flex;gap:5px;white-space:nowrap}
.info .lines span{display:block}
.info .light{font-weight:400}
.contact-h{top:884px;left:141px;font-size:15px;font-weight:700;letter-spacing:.3px}
.map{top:915px;left:141px;width:188px;height:125px;border:1px solid #e1e1e1;padding:3px;background:var(--white)}
.map div{width:100%;height:100%;background:linear-gradient(135deg,#eef0ec,#e4e6e2 60%,#dce9d5)}
.field{border:1px solid #cfcfcf;font-size:5.8px;color:#444;padding:7px 5px}
.send-btn{top:1021px;left:520px;width:60px;height:19px;font-size:8px}
.footer{top:1073px;left:0;width:720px;height:127px;background:var(--dark)}
.footer .brand{position:absolute;top:30px;width:100%;text-align:center;font-size:12px}
.social{top:1141px;left:328px;display:flex;gap:3px}
.social span{width:14px;height:14px;border-radius:50%;background:#1a1a1a}
.copy{top:1171px;width:720px;text-align:center;font-size:5.5px;color:#ddd}
</style>
</head>
<body>

<header>
  <div class="abs brand" style="top:17px;left:141px;font-size:9px">GASTHAUS<br><span style="font-size:12px">BIRKENTAL</span></div>
  <nav class="abs top-links"><span>Home</span><span>Online Check in</span><span>Blog</span><span>Contact Us</span></nav>
  <div class="abs flags"><span style="background:#2b3f8f"></span><span style="background:linear-gradient(90deg,#2b3f8f 33%,#fff 33% 66%,#d4123f 66%);width:6px"></span><span style="background:linear-gradient(90deg,#e66 50%,#fcc 50%);width:4px"></span><span style="background:linear-gradient(#333 33%,#c33 33% 66%,#e9b83b 66%)"></span></div>
  <div class="abs contact-line">CONTACT US: <b>06351/7720</b></div>
  <div class="abs email-line">EMAIL US:info@Gasthaus-Birkental.de</div>
</header>

<nav class="abs nav">
  <ul>
    <li class="active"><span>ABOUT US</span></li>
    <li><span>RESTAURANT ⌄</span></li>
    <li><span>GALLERY ⌄</span></li>
    <li><span>EVENTS ⌄</span></li>
    <li><span>CATEERS ⌄</span></li>
    <li><span>WEDDINGS</span></li>
    <li style="border:none"><span>CONTACT ⌄</span></li>
  </ul>
</nav>

<section>
  <div class="abs hero-left" role="img" aria-label="Red-tinted photo of a decorated party buffet"></div>
  <div class="abs hero-photo" role="img" aria-label="Covered terrace with orange awning and set tables"></div>
  <h1 class="abs hero-title">PARTYSERVICE</h1>
  <p class="abs hero-sub">Ihr Partyservice in Bad Lindenau und Umgebung!</p>
  <p class="abs hero-text">Sind Sie auf der Suche nach einem Partyservice in Bad Lindenau?</p>
  <a class="abs btn hero-btn">READ MORE</a>
  <div class="abs dots"><span class="on"></span><span></span><span></span></div>
</section>

<section class="abs about">
  <h2>ABOUT US</h2>
  <h3>Whole heart hosts!</h3>
  <p class="p1">Our guesthouse on the Birkental in Bad Lindenau is an oasis of relaxation and recreation. Located directly on the Birkental we welcome our guests for a few hours "holiday". Also parking facili­ties are sufficiently available.</p>
  <p class="p2">The view from the &nbsp;open terrace with about 100 seats sweeps our popular &nbsp;beach bar,</p>
</section>
<a class="abs btn about-btn">READ MORE</a>
<div class="abs about-photo" role="img" aria-label="Staff serving at a chocolate fountain buffet"></div>

<section class="abs services">
  <h2>Our Services</h2>
  <div class="rule"></div>
</section>
<div class="abs svc" style="left:141px;background:linear-gradient(180deg,#e98a2a 0 15%,#7a9a5a 15% 55%,#c89a7a)" role="img" aria-label="Restaurant terrace overlooking a green garden"></div>
<div class="abs svc" style="left:291px;background:linear-gradient(135deg,#1c1f3e,#4a4a6a 50%,#c9b88a)" role="img" aria-label="Waiter carrying a platter with sparklers"></div>
<div class="abs svc" style="left:441px;background:linear-gradient(180deg,#e8908a 0 25%,#f1ece6 25% 75%,#d9a07a)" role="img" aria-label="Wedding couple dancing in a decorated hall"></div>
<div class="abs svc-label" style="left:141px">RESTAURANTS</div>
<div class="abs svc-label" style="left:291px">CATERERS</div>
<div class="abs svc-label" style="left:441px">WEDDINGS</div>

<div class="abs gal-grey"></div>
<section class="abs gal-band">
  <h2>PHOTO GALLERY <svg width="8" height="12" viewBox="0 0 8 12"><path d="M1 1l5 5-5 5" fill="none" stroke="#fff" stroke-width="2"/></svg></h2>
</section>
<div class="abs gal-photo" role="img" aria-label="Restaurant interior with wooden tables and red chairs"></div>
<div class="abs thumb" style="top:679px;left:341px;background:linear-gradient(180deg,#f28a1c 0 20%,#c9a38e 20% 70%,#e9b82a)" role="img" aria-label="Terrace with sunflower"></div>
<div class="abs thumb" style="top:679px;left:422px;background:linear-gradient(180deg,#7a8a6a,#d9c9b0 60%,#e8d8c8)" role="img" aria-label="Beach chairs and cocktails"></div>
<div class="abs thumb" style="top:679px;left:502px;background:linear-gradient(180deg,#e98a2a 0 25%,#6a4a3a 25%,#c99a6a)" role="img" aria-label="Guests at a sparkling buffet"></div>
<div class="abs thumb" style="top:755px;left:341px;background:linear-gradient(135deg,#e8d8c8,#b89a7a 50%,#d9a05a)" role="img" aria-label="Salad bowl on the buffet"></div>
<div class="abs thumb" style="top:755px;left:422px;background:linear-gradient(180deg,#e88a8a 0 35%,#3a2a2a 35% 70%,#c97a5a)" role="img" aria-label="Wedding guests in a festive hall"></div>
<div class="abs thumb" style="top:755px;left:502px;background:linear-gradient(90deg,#4a3a2e,#6a5a4a 60%,#a8c84a)" role="img" aria-label="Dining room with set tables"></div>

<section>
  <div class="abs info" style="left:356px">
    <svg width="7" height="9" viewBox="0 0 7 9"><path d="M3.5 8.5S.5 5 .5 3.3a3 3 0 016 0C6.5 5 3.5 8.5 3.5 8.5z" fill="none" stroke="#74b844" stroke-width=".8"/><circle cx="3.5" cy="3.3" r="1" fill="#74b844"/></svg>
    <div class="lines"><span>Lena Hofbauer and</span><span>Jonas Keller</span><span class="light">Am Weiher 12</span><span class="light">67431 Bad Lindenau</span></div>
  </div>
  <div class="abs info" style="left:476px;flex-direction:column;gap:2.5px">
    <div style="display:flex;gap:6px"><svg width="7" height="7" viewBox="0 0 7 7"><path d="M1 1l1.5-.5 1 1.6-.9.7a4 4 0 001.6 1.6l.7-.9 1.6 1L6 6A5 5 0 011 1z" fill="none" stroke="#74b844" stroke-width=".7"/></svg>06351/7720</div>
    <div style="display:flex;gap:6px"><svg width="7" height="7" viewBox="0 0 7 7"><rect x="1.5" y=".5" width="4" height="2" fill="#74b844"/><rect x=".5" y="2.5" width="6" height="3" fill="#74b844"/><rect x="1.5" y="5" width="4" height="1.5" fill="#74b844"/></svg>06351/772091</div>
    <div style="display:flex;gap:6px"><svg width="7" height="7" viewBox="0 0 7 7"><rect x=".5" y="1.5" width="6" height="4.5" fill="#74b844"/><path d="M.5 1.5l3 2.5 3-2.5" stroke="#fff" stroke-width=".6" fill="none"/></svg>info@Gasthaus-Birkental.de</div>
  </div>
  <h2 class="abs contact-h">CONTACT US</h2>
  <div class="abs map"><div role="img" aria-label="Street map of the town around the guesthouse"></div></div>
  <div class="abs field" style="top:916px;left:356px;width:107px;height:18px">Name</div>
  <div class="abs field" style="top:916px;left:472px;width:107px;height:18px">Phone</div>
  <div class="abs field" style="top:943px;left:356px;width:107px;height:18px">Email</div>
  <div class="abs field" style="top:943px;left:472px;width:107px;height:18px">Subject</div>
  <div class="abs field" style="top:970px;left:356px;width:224px;height:39px">Message</div>
  <a class="abs btn send-btn">SEND</a>
</section>

<footer class="abs footer">
  <div class="brand">GASTHAUS BIRKENTAL</div>
</footer>
<div class="abs social"><span></span><span></span><span></span><span></span></div>
<p class="abs copy">Copyrights © 2019 Gasthaus Birkental. All rights reserved.</p>

</body>
</html>
```